Consulting company business cards

We have a base design, but would be willing to update. We have a new logo/"tag" that needs to be added. Current business card design is attached for reference into our "style."

Industry/Entity Type

Business

Contact Information for Business Card

Should contain name and title, office number, mobile number if appropriate, e-mail, website, physical address, and company logo.

Font styles to use
Other font styles liked:
• See current card design on GorvandBCard

Colors
0455a3
85acd3
aaaaaa

Requirements
Must have
• Our colors are navy blue, gray, and a lighter blue
Nice to have
• Design that I can easily drop in new names/titles as we hire employees.

```html
<!DOCTYPE html>
<html lang="en">
<head>
<meta charset="utf-8">
<title>Halden Business Card</title>
<link rel="stylesheet" href="https://fonts.googleapis.com/css2?family=Oswald:wght@600&family=Open+Sans:wght@400;600;700&display=swap">
<style>
  :root {
    --page: #fbfcfc;
    --royal: #1848e6;
    --sky: #88c2f3;
    --stone: #a8b4b2;
    --white: #ffffff;
  }
  * { margin: 0; padding: 0; box-sizing: border-box; }
  html, body { width: 1200px; height: 1000px; overflow: hidden; background: var(--page); }
  .canvas { position: relative; width: 1200px; height: 1000px; }

  /* Front side */
  .card-front {
    position: absolute; left: 54px; top: 38px; width: 478px; height: 258px;
    background: var(--royal); overflow: hidden;
  }
  .card-front .brand-band {
    position: absolute; left: 0; top: 138px; width: 100%; height: 110px; background: var(--stone);
  }
  .card-front .brand-name {
    position: absolute; left: 19px; top: 4px;
    font-family: "Oswald", sans-serif; font-weight: 600; font-size: 62px; line-height: 1;
    letter-spacing: 2px; color: var(--royal);
  }
  .card-front .brand-mark {
    position: absolute; left: 236px; top: 12px; width: 56px; height: 56px;
    border-radius: 50%; background: var(--royal);
  }
  .card-front .brand-tagline {
    position: absolute; left: 20px; top: 82px;
    font-family: "Open Sans", sans-serif; font-size: 13px; letter-spacing: 1.3px; color: var(--royal);
  }

  /* Back side */
  .card-back {
    position: absolute; left: 657px; top: 38px; width: 476px; height: 257px;
    background: var(--sky); overflow: hidden; text-align: center; color: var(--royal);
    font-family: "Open Sans", sans-serif;
  }
  .person-name {
    position: absolute; left: 0; top: 0; width: 100%;
    font-size: 27px; line-height: 32px; letter-spacing: 0.5px; font-weight: 400;
  }
  .person-name strong { font-weight: 700; }
  .person-title {
    position: absolute; left: 0; top: 31px; width: 100%; height: 17px; background: var(--royal);
    color: var(--white); font-size: 14px; line-height: 17px; font-weight: 600; letter-spacing: 0.5px;
  }
  .contact-row {
    position: absolute; left: 0; width: 100%; height: 48px;
    font-family: Arial, sans-serif; font-size: 9.5px;
  }
  .contact-row svg { display: block; margin: 0 auto 3px; }
  .contact-row.phone { top: 56px; }
  .contact-row.mail { top: 108px; }
  .contact-row.place { top: 157px; }
  .divider { position: absolute; left: 0; width: 100%; height: 2px; background: var(--royal); }
  .divider.one { top: 96px; }
  .divider.two { top: 145px; }
  .footer-band {
    position: absolute; left: 0; top: 198px; width: 100%; height: 59px; background: var(--royal); color: var(--white);
  }
  .footer-band .web {
    position: absolute; left: 0; top: 3px; width: 100%; font-size: 6.5px; letter-spacing: 2.4px;
  }
  .footer-band .brand-name {
    position: absolute; left: 187px; top: 14px;
    font-family: "Oswald", sans-serif; font-weight: 600; font-size: 24px; line-height: 1; letter-spacing: 1px;
  }
  .footer-band .brand-mark {
    position: absolute; left: 271px; top: 17px; width: 20px; height: 20px; border-radius: 50%; background: var(--white);
  }
  .footer-band .brand-tagline {
    position: absolute; left: 187px; top: 42px; font-size: 5px; letter-spacing: 0.5px;
  }
</style>
</head>
<body>
<div class="canvas">

  <section class="card-front">
    <div class="brand-band">
      <div class="brand-name">HALDEN</div>
      <div class="brand-mark"></div>
      <div class="brand-tagline">A CLOUD CONSULTING COMPANY</div>
    </div>
  </section>

  <section class="card-back">
    <div class="person-name">FIRST <strong>LAST</strong></div>
    <div class="person-title">OFFICE MANAGER</div>

    <div class="contact-row phone">
      <svg width="10" height="15" viewBox="0 0 10 15" aria-hidden="true">
        <rect x="1" y="0.75" width="8" height="13.5" rx="1.2" fill="none" stroke="currentColor" stroke-width="1.3"/>
        <line x1="4" y1="12" x2="6" y2="12" stroke="currentColor" stroke-width="1"/>
      </svg>
      O 555.014.3847 / F 555.014.3852
    </div>
    <div class="divider one"></div>

    <div class="contact-row mail">
      <svg width="14" height="10" viewBox="0 0 14 10" aria-hidden="true">
        <rect x="0" y="0" width="14" height="10" fill="currentColor"/>
        <polyline points="0.5,0.5 7,5.5 13.5,0.5" fill="none" stroke="#88c2f3" stroke-width="1"/>
      </svg>
      example@mail.com
    </div>
    <div class="divider two"></div>

    <div class="contact-row place">
      <svg width="11" height="15" viewBox="0 0 11 15" aria-hidden="true">
        <path d="M5.5 0.5C2.7 0.5 0.5 2.7 0.5 5.5 0.5 9 5.5 14.5 5.5 14.5S10.5 9 10.5 5.5C10.5 2.7 8.3 0.5 5.5 0.5Z" fill="currentColor"/>
        <circle cx="5.5" cy="5.3" r="2" fill="#88c2f3"/>
      </svg>
      1850 W ORCHARD AVE LAKEVIEW OHIO 45011
    </div>

    <div class="footer-band">
      <div class="web">www.website.com</div>
      <div class="brand-name">HALDEN</div>
      <div class="brand-mark"></div>
      <div class="brand-tagline">A CLOUD CONSULTING COMPANY</div>
    </div>
  </section>

</div>
</body>
</html>
```